Software design for senior-friendly computer

Our software helps elderly people use the computer even if they are afraid of technology and have never used a computer before. We install the software on a Windows PC and our software holds a number of applications for basic tasks.

The software is old and needs a facelift to become more light and modern, and to avoid patronizing the audience. But the new design must still be "friendly", non-technical and make the user feel safe if he/she is a bit afraid of computers.

The screen resolution is 1600x900. This is not a complete redo of the software, so please avoid moving the buttons and other objects around.

We need your redesign of attached 6 screenshots (2 of which are the main menu). The rest of the apps we plan to do ourselves based on the winning design.

Target Market(s)

Age group 50+

Industry/Entity Type

Computer

Font styles to use
Sans Serif

Requirements
Must have
• Friendly, modern (but not too modern) look. Must make the user feel safe and comfortable using the computer even if he/she is a bit afraid of technology.
• Design must include the red/yellow velo- logo shown in the screenshots.

```html
<!DOCTYPE html>
<html lang="en">
<head>
<meta charset="utf-8">
<title>velo- Search &amp; Find</title>
<link rel="stylesheet" href="https://fonts.googleapis.com/css2?family=Source+Sans+3:ital,wght@0,400;0,600;0,700;1,400&display=swap">
<style>
:root{
  --red:#c8171e;
  --yellow:#f5b81c;
  --orange:#e0561a;
  --white:#ffffff;
  --ink:#1e1e1e;
  --row:#e6e6e6;
  --row-head:#ececec;
  --side:#262626;
  --side-line:#555;
  --thumb:#555555;
  --bg-top:#232323;
  --bg-bottom:#3a3a3a;
}
*{box-sizing:border-box;margin:0;padding:0}
html,body{width:1200px;height:675px;overflow:hidden}
body{font-family:"Source Sans 3",sans-serif;background:linear-gradient(180deg,var(--bg-top),var(--bg-bottom));position:relative;color:var(--ink)}
.topbar{position:absolute;left:0;top:0;width:1200px;height:75px;background:var(--red);color:var(--white)}
.home-btn{position:absolute;left:0;top:0;width:101px;height:75px;text-align:center;font-size:22px;line-height:1}
.home-btn svg{display:block;margin:9px auto 3px}
.brand{position:absolute;left:101px;top:0;width:185px;height:75px;background:var(--white);display:flex;align-items:center;justify-content:center;gap:8px}
.brand-name{color:var(--red);font-weight:700;font-size:42px;letter-spacing:-1px}
.brand-dot{width:20px;height:20px;border-radius:50%;background:var(--yellow);margin-top:8px}
.clock{position:absolute;left:436px;width:300px;top:7px;text-align:center;font-size:29px;line-height:1.05}
.clock .date{font-size:23px}
.user{position:absolute;right:104px;top:11px;text-align:right;font-size:25px;line-height:1.1}
.user .mail{font-size:21px}
.avatar{position:absolute;left:1117px;top:2px;width:71px;height:71px;border-radius:50%;background:radial-gradient(circle at 50% 40%,#9aa3b5,#5d6577)}

.sidebar{position:absolute;left:14px;top:99px;width:295px;height:559px;border:1px solid #555;background:#222}
.cat{position:absolute;left:0;width:293px;height:52px;border-bottom:1px solid var(--side-line);background:var(--side);color:var(--white);display:flex;align-items:center;gap:14px;padding-left:17px;font-size:21px}
.cat svg{width:26px;height:26px;flex:none}
.cat.is-active{left:-1px;top:-1px;width:311px;height:50px;background:var(--white);color:var(--ink);border:3px solid var(--yellow);border-right:none}

.favourites{position:absolute;left:324px;top:98px;width:560px;height:562px;border:3px solid var(--yellow);border-left:none;background:var(--white);overflow:hidden}
.featured{position:absolute;left:15px;top:8px;width:533px;height:173px;border:2px solid #ccc;background:var(--white)}
.featured-head{height:45px;background:var(--row-head);display:flex;align-items:center;padding-left:16px;font-size:22px}
.featured-head .engine{font-weight:600;color:#3a6fd8;margin-right:10px}
.url{font-size:16px;color:#444;margin:4px 0 0 19px}
.hint{font-size:18px;line-height:1.15;margin:2px 0 0 19px;width:500px}
.search-box{position:absolute;left:16px;top:117px;width:380px;height:39px;border:1px solid #bbb;font-style:italic;color:#888;font-size:16px;padding:8px 12px}
.search-btn{position:absolute;left:406px;top:117px;width:115px;height:39px;background:#dcdcdc;border:1px solid #ccc;text-align:center;font-size:20px;line-height:37px}
.show-btn{position:absolute;left:509px;width:127px;height:32px;background:var(--yellow);display:flex;align-items:center;justify-content:center;gap:6px;font-size:18px}
.toggle{position:absolute;left:664px;width:30px;height:30px;border-radius:50%;border:2px solid #aaa;background:var(--white);display:flex;align-items:center;justify-content:center}
.featured .show-btn{left:409px;top:6px}
.featured .toggle{left:596px;top:7px}
.fav{position:absolute;left:15px;width:533px;height:45px;background:var(--row)}
.fav .thumb{position:absolute;left:8px;top:8px;width:76px;height:28px;background:var(--thumb)}
.fav .name{position:absolute;left:116px;top:0;line-height:45px;font-size:22px}
.fav .show-btn{left:339px;top:7px}
.fav .toggle{left:493px;top:7px}

.pager{position:absolute;left:324px;top:606px;width:560px;height:54px;background:var(--red)}
.pager-btn{position:absolute;top:6px;height:42px;display:flex;align-items:center;justify-content:center;gap:8px;font-size:23px}
.pager-up{left:9px;width:94px;background:var(--orange);color:#f5a070;border:2px solid #d04a12}
.pager-down{left:416px;width:126px;background:var(--yellow);color:var(--ink);border:2px solid #333}

.info{position:absolute;left:902px;top:99px;width:278px;height:447px;background:var(--white);font-size:13.2px;line-height:1.4;padding:115px 9px 0 9px;color:#333}
.info-badge{position:absolute;left:92px;top:13px;width:82px;height:82px;border-radius:50%;background:var(--yellow)}
.info p{margin-bottom:17px}
</style>
</head>
<body>
<header class="topbar">
  <div class="home-btn">
    <svg width="40" height="32" viewBox="0 0 40 32"><path d="M4 16 L20 3 L36 16" fill="none" stroke="#fff" stroke-width="4" stroke-linejoin="round"/><path d="M9 15 V30 H17 V21 H23 V30 H31 V15" fill="#fff"/></svg>
    Home
  </div>
  <div class="brand"><span class="brand-name">velo</span><span class="brand-dot"></span></div>
  <div class="clock"><div>09:39:50 AM</div><div class="date">Tuesday 02/14/2017</div></div>
  <div class="user"><div>Henrik Molvang</div><div class="mail">hmo@velomail.example</div></div>
  <div class="avatar" role="img" aria-label="User profile picture"></div>
</header>

<nav class="sidebar">
  <div class="cat is-active" style="top:-1px"><svg viewBox="0 0 26 26"><circle cx="10" cy="10" r="7.5" fill="none" stroke="#1e1e1e" stroke-width="3"/><path d="M15.5 15.5 L23 23" stroke="#1e1e1e" stroke-width="3.5" stroke-linecap="round"/></svg>Search &amp; Find</div>
  <div class="cat" style="top:52px"><svg viewBox="0 0 26 26"><path d="M13 1 L16.5 9 L25 9.8 L18.5 15.5 L20.5 24 L13 19.5 L5.5 24 L7.5 15.5 L1 9.8 L9.5 9 Z" fill="#f5b81c"/></svg>Personal Favorites</div>
  <div class="cat" style="top:104px"><svg viewBox="0 0 26 26"><rect x="2" y="11" width="6" height="13" rx="1" fill="#f0a868"/><path d="M9 11 L14 2 Q17 2 16 8 H23 Q25 9 24 12 L22 22 Q21 24 19 24 H9 Z" fill="#f4b27a"/></svg>Recommended</div>
  <div class="cat" style="top:156px"><svg viewBox="0 0 26 26"><path d="M1 9 L13 2 L25 9 Z M2 22 H24 V25 H2 Z" fill="#ddd"/><rect x="4" y="11" width="3" height="10" fill="#ddd"/><rect x="9.5" y="11" width="3" height="10" fill="#ddd"/><rect x="14" y="11" width="3" height="10" fill="#ddd"/><rect x="19" y="11" width="3" height="10" fill="#ddd"/></svg>Government</div>
  <div class="cat" style="top:208px"><svg viewBox="0 0 26 26"><rect x="6" y="5" width="14" height="16" rx="2" fill="#3fae4c"/><circle cx="13" cy="13" r="4" fill="#222"/><path d="M1 13 H6 M20 13 H25" stroke="#3fae4c" stroke-width="3"/></svg>Internet Banking</div>
  <div class="cat" style="top:260px"><svg viewBox="0 0 26 26"><path d="M2 3 L24 2 L14 24 Z" fill="none" stroke="#8fb7e8" stroke-width="2.5" stroke-linejoin="round"/><path d="M2 3 L14 14" stroke="#8fb7e8" stroke-width="2"/></svg>News</div>
  <div class="cat" style="top:312px"><svg viewBox="0 0 26 26"><rect x="1" y="7" width="24" height="13" rx="6.5" fill="#f08a9a"/><path d="M6 13.5 H11 M8.5 11 V16" stroke="#222" stroke-width="2"/><circle cx="17" cy="12" r="1.5" fill="#222"/><circle cx="20" cy="15" r="1.5" fill="#222"/></svg>Games &amp; Hobbies</div>
  <div class="cat" style="top:364px"><svg viewBox="0 0 26 26"><path d="M13 24 L3 13 Q-1 6 6 3 Q10 2 13 6 Q16 2 20 3 Q27 6 23 13 Z" fill="#e0402a"/><path d="M5 13 H10 L12 9 L14 17 L16 13 H21" fill="none" stroke="#222" stroke-width="1.6"/></svg>Health</div>
  <div class="cat" style="top:416px"><svg viewBox="0 0 26 26"><circle cx="13" cy="10" r="8" fill="#e8803a"/><rect x="11.5" y="14" width="3" height="11" fill="#c45e20"/></svg>Out and About</div>
</nav>

<main class="favourites">
  <section class="featured">
    <div class="featured-head"><span class="engine">Seekwell</span>Search</div>
    <div class="show-btn"><svg width="26" height="16" viewBox="0 0 26 16"><path d="M1 8 Q13 -4 25 8 Q13 20 1 8 Z" fill="none" stroke="#1e1e1e" stroke-width="2.4"/><circle cx="13" cy="8" r="4" fill="#1e1e1e"/></svg>Show Page</div>
    <div class="toggle"><svg width="14" height="14"><path d="M2 7 H12" stroke="#999" stroke-width="2"/></svg></div>
    <div class="url">https://www.seekwell.example</div>
    <p class="hint">Here you can search for anything you wish; simply type in one or more words, separated by space, and click search.</p>
    <div class="search-box">Click here and enter search word(s)</div>
    <div class="search-btn">Search</div>
  </section>

  <div class="fav" style="top:193px"><div class="thumb"></div><div class="name">Enter Address</div><div class="show-btn"><svg width="26" height="16" viewBox="0 0 26 16"><path d="M1 8 Q13 -4 25 8 Q13 20 1 8 Z" fill="none" stroke="#1e1e1e" stroke-width="2.4"/><circle cx="13" cy="8" r="4" fill="#1e1e1e"/></svg>Show Page</div><div class="toggle"><svg width="14" height="14"><path d="M2 7 H12 M7 2 V12" stroke="#999" stroke-width="2"/></svg></div></div>
  <div class="fav" style="top:253px"><div class="thumb"></div><div class="name">Replay Radio</div><div class="show-btn"><svg width="26" height="16" viewBox="0 0 26 16"><path d="M1 8 Q13 -4 25 8 Q13 20 1 8 Z" fill="none" stroke="#1e1e1e" stroke-width="2.4"/><circle cx="13" cy="8" r="4" fill="#1e1e1e"/></svg>Show Page</div><div class="toggle"><svg width="14" height="14"><path d="M2 7 H12 M7 2 V12" stroke="#999" stroke-width="2"/></svg></div></div>
  <div class="fav" style="top:315px"><div class="thumb"></div><div class="name">Local Library</div><div class="show-btn"><svg width="26" height="16" viewBox="0 0 26 16"><path d="M1 8 Q13 -4 25 8 Q13 20 1 8 Z" fill="none" stroke="#1e1e1e" stroke-width="2.4"/><circle cx="13" cy="8" r="4" fill="#1e1e1e"/></svg>Show Page</div><div class="toggle"><svg width="14" height="14"><path d="M2 7 H12 M7 2 V12" stroke="#999" stroke-width="2"/></svg></div></div>
  <div class="fav" style="top:375px"><div class="thumb"></div><div class="name">Classified Ads</div><div class="show-btn"><svg width="26" height="16" viewBox="0 0 26 16"><path d="M1 8 Q13 -4 25 8 Q13 20 1 8 Z" fill="none" stroke="#1e1e1e" stroke-width="2.4"/><circle cx="13" cy="8" r="4" fill="#1e1e1e"/></svg>Show Page</div><div class="toggle"><svg width="14" height="14"><path d="M2 7 H12 M7 2 V12" stroke="#999" stroke-width="2"/></svg></div></div>
  <div class="fav" style="top:435px"><div class="thumb"></div><div class="name">Country Rail</div><div class="show-btn"><svg width="26" height="16" viewBox="0 0 26 16"><path d="M1 8 Q13 -4 25 8 Q13 20 1 8 Z" fill="none" stroke="#1e1e1e" stroke-width="2.4"/><circle cx="13" cy="8" r="4" fill="#1e1e1e"/></svg>Show Page</div><div class="toggle"><svg width="14" height="14"><path d="M2 7 H12 M7 2 V12" stroke="#999" stroke-width="2"/></svg></div></div>
  <div class="fav" style="top:495px"><div class="thumb"></div><div class="show-btn" style="width:127px"></div></div>
</main>

<div class="pager">
  <div class="pager-btn pager-up">Up<svg width="26" height="26" viewBox="0 0 26 26"><circle cx="13" cy="13" r="12" fill="#d04a12"/><path d="M13 5 L20 13 H16 V20 H10 V13 H6 Z" fill="#f5a070"/></svg></div>
  <div class="pager-btn pager-down">Down<svg width="26" height="26" viewBox="0 0 26 26"><circle cx="13" cy="13" r="12" fill="#1e1e1e"/><path d="M13 21 L20 13 H16 V6 H10 V13 H6 Z" fill="#f5b81c"/></svg></div>
</div>

<aside class="info">
  <div class="info-badge"><svg width="82" height="82" viewBox="0 0 82 82"><circle cx="41" cy="23" r="6" fill="#fff"/><path d="M34 33 H45 V57 H49 V62 H33 V57 H37 V38 H34 Z" fill="#fff"/></svg></div>
  <p>Select a category from the list to the left. You will see a list of favourites (pre-chosen websites) that correspond to that category in the centre of the screen. Click <b>Show Page</b> next to the favourite you want to have shown.</p>
  <p>If you wish to search the internet for a specific site, click the category <b>Search and Find</b> and the favourite <b>Seekwell</b>.</p>
  <p>If you know the website's address, click the favourite <b>Enter Address</b> and type the address.</p>
  <p>Click the interactive user guide for more help with the internet.</p>
</aside>
</body>
</html>
```